1 Campaign Poster A0 for 8,000 Model Builders for Eurasia

I need a poster explaining and advertising the campaign 8,000 Model Builders for Eurasia - as presented on Ticketloom (multiple events), Friendwall (campaign HQ), Quillpost (blog). A summary with links is here: http://blog.cortivex.example/2018/04/17/from-science-to-data-science-how-do-i-best-move-to-industry-as-a-phd-or-postdoc/

The target crowd is STEM PhDs and Postdocs in Europe - a very diverse, gender-balanced, and a global crowd that has AI talent: the capacity to create the next generation of AI-driven products.

I have high-quality pictures from the workshops that I can share (but apparently not upload because too wide).
In parallel, a video is being produced next week.
Updates

We want to change the format of the poster and optimize for A3 297 x 420 mm 0,12474 qm 3508 x 4961 Pixel 300 ppi 1754 x 2480 Pixel 150 ppi

Target Market(s)

a) PhDs and workshop participants as workshop participants
b) Universities or employers as workshop host.

Industry/Entity Type

Education

Font styles to use
Sans Serif

Colors

Designer to choose colors to be used in the design.

Requirements
Must have
• 1. Feature the free 'Lab to Model Lab' workshop series we run in Europe with the main takeaways:
• - A roadmap to transition to Data Science and AI within 6-9 months
• - Inspiration on how to prepare a CV that gets you interviews with hiring manager
• - Insight into any gap you might have (if any) for getting a first and good position in industry and startups
• 2. Show the roadmap and its four steps of exploration, orientation, training and career start (explained in the article + roadmap graphic) - http://blog.cortivex.example/2018/04/17/from-science-to-data-science-how-do-i-best-move-to-industry-as-a-phd-or-postdoc/
• 3. Call to action
• a) PhDs and Postdocs - go to modelbuilder.ticketloom.example and register for the next event
• b) University or employer of data scientists: Host our workshop?!
Nice to have
• What I am looking for is a poster that flows (as in 'transition' from academia to industry; 'move' from Lab to Model Lab) towards the call for action.
• I have pictures etc. that can be reused. They are professional, high-resolution etc. but wider than 4096 px.

```html
<!DOCTYPE html>
<html lang="en">
<head>
<meta charset="utf-8">
<title>PhD career workshop</title>
<link rel="stylesheet" href="https://fonts.googleapis.com/css2?family=Source+Sans+3:wght@300;400;600;700&family=Open+Sans:wght@700&display=swap">
<style>
  :root {
    --cream: #fdf6ea;
    --peach: #f8dcb6;
    --peach-deep: #f3c995;
    --orange-label: #f5a62b;
    --title-teal: #17484f;
    --tick-teal: #2a7d82;
    --text-dark: #2a2a2a;
    --step-gray: #4b4e53;
    --step-gray-dark: #35373b;
    --explore: #f2834f;
    --orientation: #f7b52b;
    --training: #1fb8c8;
    --career: #1aa69a;
    --footer: #1d6b6d;
    --white: #ffffff;
    --art-yellow: #f6cf63;
    --art-teal: #9cc9c8;
    --skin: #e9c3a3;
    --shirt: #eceae6;
    --denim: #46618a;
    --floor-light: #dca56f;
    --floor-dark: #b97a45;
  }
  * { box-sizing: border-box; margin: 0; padding: 0; }
  html, body { width: 924px; height: 1200px; overflow: hidden; background: #ececec; }
  .poster {
    position: relative;
    width: 924px;
    height: 1200px;
    overflow: hidden;
    font-family: "Source Sans 3", sans-serif;
    background: radial-gradient(ellipse at 62% 30%, var(--cream) 0%, var(--peach) 60%, var(--peach-deep) 100%);
  }
  .eyebrow {
    position: absolute; top: 44px; left: 0; width: 100%;
    display: flex; justify-content: center; align-items: center; gap: 10px;
    font-weight: 700; font-size: 40px; color: var(--orange-label); letter-spacing: 0.3px;
  }
  .eyebrow::before, .eyebrow::after {
    content: ""; width: 136px; height: 1.5px; background: var(--orange-label);
  }
  .title {
    position: absolute; top: 86px; left: 0; width: 100%; text-align: center;
    font-family: "Open Sans", sans-serif; font-weight: 700; font-size: 61px;
    color: var(--title-teal); letter-spacing: 0.5px;
  }
  .network-art {
    position: absolute; left: 20px; top: 200px; width: 442px; height: 278px;
    border-radius: 14px;
    background: linear-gradient(135deg, var(--art-teal) 0%, var(--art-yellow) 55%, #f3b66b 100%);
    opacity: 0.75;
  }
  .photo-floor {
    position: absolute; left: 0; top: 960px; width: 924px; height: 148px;
    background: linear-gradient(to bottom, var(--floor-light) 0%, var(--floor-dark) 100%);
  }
  .photo-person {
    position: absolute; left: 0; top: 512px; width: 522px; height: 596px;
    border-radius: 0 18px 0 0;
    background: linear-gradient(to bottom, var(--skin) 0%, var(--shirt) 40%, var(--shirt) 62%, var(--denim) 78%, var(--denim) 100%);
  }
  .benefits { position: absolute; right: 20px; top: 222px; width: 540px; list-style: none; }
  .benefit {
    display: flex; justify-content: flex-end; align-items: center; gap: 22px;
    height: 96px; margin-bottom: 30px;
  }
  .benefit-text {
    text-align: right; font-size: 23px; line-height: 29px; color: var(--text-dark); font-weight: 400;
  }
  .benefit-tick { width: 70px; height: 64px; flex: none; }
  .roadmap { position: absolute; left: 510px; top: 670px; width: 400px; height: 340px; }
  .roadmap text { font-family: "Source Sans 3", sans-serif; fill: var(--white); }
  .step-label { font-size: 14px; font-weight: 400; }
  .step-number { font-size: 32px; font-weight: 300; }
  .step-name { font-size: 18px; font-weight: 700; }
  .footer-rule { position: absolute; left: 0; top: 1108px; width: 100%; height: 5px; background: var(--white); }
  .footer {
    position: absolute; left: 0; top: 1113px; width: 100%; height: 87px;
    background: var(--footer); color: var(--white);
    display: flex; flex-direction: column; justify-content: center; align-items: center;
    font-size: 21px; line-height: 28px;
  }
  .footer strong { font-weight: 700; }
</style>
</head>
<body>
<main class="poster">
  <div class="eyebrow">WORKSHOP</div>
  <h1 class="title">PhD career workshop</h1>

  <div class="network-art" role="img" aria-label="Hand-drawn colourful network graph doodles around large yellow letters AI"></div>
  <div class="photo-floor" role="img" aria-label="Warm wooden floor of the workshop photo"></div>
  <div class="photo-person" role="img" aria-label="Photo of a young woman in glasses and a white T-shirt sitting cross-legged with a laptop, looking up thoughtfully"></div>

  <ul class="benefits">
    <li class="benefit">
      <p class="benefit-text">A roadmap to transition<br>to Data Science and AI<br>in 6-9 months</p>
      <svg class="benefit-tick" viewBox="0 0 70 64" aria-hidden="true"><path d="M4 30 L26 56 Q40 20 66 4" fill="none" stroke="var(--tick-teal)" stroke-width="6" stroke-linecap="round" stroke-linejoin="round"/></svg>
    </li>
    <li class="benefit">
      <p class="benefit-text">Inspiration on how to<br>prepare a CV that gets you an<br>interview with a hiring manager</p>
      <svg class="benefit-tick" viewBox="0 0 70 64" aria-hidden="true"><path d="M4 30 L26 56 Q40 20 66 4" fill="none" stroke="var(--tick-teal)" stroke-width="6" stroke-linecap="round" stroke-linejoin="round"/></svg>
    </li>
    <li class="benefit">
      <p class="benefit-text">Insight into closing the skills gap<br>for your first position in the<br>industry or a startup</p>
      <svg class="benefit-tick" viewBox="0 0 70 64" aria-hidden="true"><path d="M4 30 L26 56 Q40 20 66 4" fill="none" stroke="var(--tick-teal)" stroke-width="6" stroke-linecap="round" stroke-linejoin="round"/></svg>
    </li>
  </ul>

  <svg class="roadmap" viewBox="0 0 400 340" role="img" aria-label="Roadmap in four steps: explore data science, industry orientation, skills training, start your career">
    <g stroke="var(--step-gray)" stroke-width="2">
      <line x1="338" y1="74" x2="338" y2="96"/>
      <line x1="60" y1="158" x2="60" y2="180"/>
      <line x1="338" y1="242" x2="338" y2="262"/>
    </g>

    <rect x="9" y="9" width="377" height="66" rx="33" fill="var(--step-gray)"/>
    <polygon points="108,9 140,9 115,42 140,75 108,75 88,42" fill="var(--step-gray-dark)"/>
    <path d="M140 9 H353 A33 33 0 0 1 353 75 H140 L115 42 Z" fill="var(--explore)"/>
    <text class="step-label" x="38" y="35">STEP</text>
    <text class="step-number" x="36" y="66">01</text>
    <text class="step-name" x="250" y="38" text-anchor="middle">EXPLORE DATA</text>
    <text class="step-name" x="250" y="62" text-anchor="middle">SCIENCE</text>

    <rect x="9" y="93" width="377" height="66" rx="33" fill="var(--step-gray)"/>
    <polygon points="255,93 287,93 307,126 287,159 255,159 280,126" fill="var(--step-gray-dark)"/>
    <path d="M255 93 H42 A33 33 0 0 0 42 159 H255 L280 126 Z" fill="var(--orientation)"/>
    <text class="step-label" x="305" y="119">STEP</text>
    <text class="step-number" x="303" y="150">02</text>
    <text class="step-name" x="142" y="122" text-anchor="middle">INDUSTRY</text>
    <text class="step-name" x="142" y="146" text-anchor="middle">ORIENTATION</text>

    <rect x="9" y="177" width="377" height="66" rx="33" fill="var(--step-gray)"/>
    <polygon points="108,177 140,177 115,210 140,243 108,243 88,210" fill="var(--step-gray-dark)"/>
    <path d="M140 177 H353 A33 33 0 0 1 353 243 H140 L115 210 Z" fill="var(--training)"/>
    <text class="step-label" x="38" y="203">STEP</text>
    <text class="step-number" x="36" y="234">03</text>
    <text class="step-name" x="250" y="206" text-anchor="middle">SKILLS</text>
    <text class="step-name" x="250" y="230" text-anchor="middle">TRAINING</text>

    <rect x="9" y="261" width="377" height="66" rx="33" fill="var(--step-gray)"/>
    <polygon points="255,261 287,261 307,294 287,327 255,327 280,294" fill="var(--step-gray-dark)"/>
    <path d="M255 261 H42 A33 33 0 0 0 42 327 H255 L280 294 Z" fill="var(--career)"/>
    <text class="step-label" x="305" y="287">STEP</text>
    <text class="step-number" x="303" y="318">04</text>
    <text class="step-name" x="142" y="290" text-anchor="middle">START YOUR</text>
    <text class="step-name" x="142" y="314" text-anchor="middle">CAREER</text>
  </svg>

  <div class="footer-rule"></div>
  <footer class="footer">
    <p>Workshop registration at <strong>modelbuilder.ticketloom.example</strong></p>
    <p>Community page at <strong>friendwall.example/modelbuilderseurasia/</strong></p>
  </footer>
</main>
</body>
</html>
```